Modern Design for mouse mat (used as Give Away) for IT Company

We are an IT Company in Lucerne. We want to replace our current mouse mat by a new one. The new mouse mat is mouse mat and cleaning cloth in one. For the new mouse mat we are now looking for a nice design on it, but which is still alike the old one. The base colour of the mouse mat will be red (similar to rgb 229,53,44). Our company logo (white) should of course find a place on the mousemat as well as a nice slogan and a grafic (white).

The uploaded files are a picture of de current mouse mat, samples of the new one and a sketch how the layout of the new one could be (green line are only to show the space for the grafic).

We'd like to start with the mouse mat for our web developement / web redesign services. There we focus on inbound marketing. Our target is to develope & realize individual websites for clients which work in the B2B segment. The websites should be focussed on the users. This we realize with inbound marketing instruments. The slogan/message should contain something about that, but it should be easy understanding. Please do not use "inbound marketing" in the slogan / message. You also find a picture "Picture for Sketch" witch should be the graffic on the mousepad. This graffic should only be used in white & if possible should every screen contain the same picture(not as at the moment).

Target Market(s)

normal society

Industry/Entity Type

It Company

Font styles to use
Other font styles liked:
• FS Albert

Colors
ec1f27
ffffff

Requirements
Must have
• Slogan, Logo, grafic
Nice to have
• overloaded layout

```html
<!DOCTYPE html>
<html lang="de">
<head>
<meta charset="utf-8">
<title>Lumora IT Solutions – Mousepad</title>
<link rel="stylesheet" href="https://fonts.googleapis.com/css2?family=Fira+Sans:ital,wght@0,300;0,400;0,600;0,700;1,300&display=swap">
<style>
  :root {
    --brand-red: #e5352c;
    --paper-white: #ffffff;
    --device-dark: #2a2a2a;
    --device-mid: #7b7c76;
    --font-main: "Fira Sans", "Helvetica Neue", Arial, sans-serif;
  }
  html, body {
    margin: 0;
    padding: 0;
    overflow: hidden;
  }
  .mousepad {
    position: relative;
    width: 1200px;
    height: 750px;
    background: var(--brand-red);
    color: var(--paper-white);
    font-family: var(--font-main);
    overflow: hidden;
  }
  .brand {
    position: absolute;
    right: 36px;
    top: 34px;
    text-align: right;
  }
  .brand-name {
    display: block;
    font-weight: 700;
    font-size: 92px;
    line-height: 1;
    letter-spacing: -1px;
  }
  .brand-descriptor {
    display: block;
    margin-top: 2px;
    font-weight: 300;
    font-size: 25px;
    letter-spacing: 1px;
  }
  .message {
    position: absolute;
    left: 36px;
    top: 196px;
  }
  .headline {
    margin: 0;
    font-weight: 600;
    font-size: 62px;
    line-height: 74px;
    letter-spacing: -0.5px;
  }
  .subline {
    margin: 14px 0 0 3px;
    font-weight: 300;
    font-style: italic;
    font-size: 38px;
    line-height: 50px;
  }
  .devices-visual {
    position: absolute;
    left: 548px;
    top: 368px;
    width: 632px;
    height: 340px;
    border-radius: 14px;
    background: radial-gradient(ellipse at 50% 40%, var(--device-mid) 0%, var(--device-dark) 78%);
  }
</style>
</head>
<body>
  <main class="mousepad">
    <div class="brand">
      <span class="brand-name">Lumora</span>
      <span class="brand-descriptor">IT SOLUTIONS</span>
    </div>

    <section class="message">
      <h1 class="headline">Für den ersten<br>Eindruck gibt es keine<br>zweite Chance</h1>
      <p class="subline">Optimieren Sie deshalb<br>Ihre Website regelmässig!</p>
    </section>

    <div class="devices-visual" role="img" aria-label="Illustration: Monitor, Tablet, Smartphone und Laptop mit derselben responsiven Website in Grün und Grau"></div>
  </main>
</body>
</html>
```